Business Card Design Project

We need a business card design for an existing company that we have just acquired and need to refresh and revamp to give it a fresher, more modern, and professional image.
We are a niche high end management consulting firm working with large BRQ300 type companies.
Our services include commercial advisory, change management, culture development, leadership and team development, and training.
The old website for this company is www.kelmorvo-grp.example that will give you a better understanding of what this business does.
However, we have updated the logo and are changing the website as well so your design for the business card might influence how we design the website.
Our corporate colours are red and white but we also use light grey, black, and dark blue (occasionally) on our stationery.
The final design should communicate partnership, creativity, performance, insight, and change.
Updates

Some of you were having trouble viewing the original logo file.  I have now updated another file with .jpg version of logo.  Hope this helps.

Target Market(s)

We are a consultancy firm servicing Top BRQ or Vantage 300 type companies.

Industry/Entity Type

Management Consulting

Requirements
Must have
• Design must have all contact information and logo on 1 side of card. Back of card should be solid colour or watermarked only - i.e. no real writing on back of card.
Cards must be scannable by those new business card scanners that store the image electronically.
Will be printing on high quality paper with matte finish so design must be high definition to allow good printing.
Card must be normal business card size (no small or 3/4 sized cards).
Nice to have
• A design that has a bit of 'movement' in it rather than look blockish and rigid. Not sure how this can be done but something that gives the card a sense of flow because our work all about integrating and synthesising the 'hard' commercial aspects with the 'soft' human (psychological) dimensions into contracts and projects.
Design should be transferrable to stationery and website to the extent possible/sensible.
Should not have
• - 'old fashioned' or 'girly' or 'comical' fonts.

- no clip art like images

- no superfluous design features that convey no real message or idea.

```html
<!DOCTYPE html>
<html lang="en">
<head>
<meta charset="utf-8">
<title>Kelmorvo Group – Business Card</title>
<link rel="stylesheet" href="https://fonts.googleapis.com/css2?family=Arimo:wght@400;700&display=swap">
<style>
  :root {
    --stage: #2a2a2c;
    --brand-red: #b8202a;
    --card-paper: #f6eeec;
    --card-paper-edge: #efe2df;
    --ink: #2b2b2b;
    --rule-white: rgba(255,255,255,0.85);
  }
  * { margin: 0; padding: 0; box-sizing: border-box; }
  html, body { width: 1200px; height: 900px; overflow: hidden; }
  body {
    background: var(--stage);
    font-family: "Arimo", Arial, sans-serif;
    position: relative;
  }

  .card { position: absolute; border-radius: 2px; }

  .card-back {
    left: 140px; top: 110px;
    width: 560px; height: 342px;
    background: var(--brand-red);
  }

  .card-front {
    left: 330px; top: 380px;
    width: 700px; height: 427px;
    background: linear-gradient(135deg, var(--card-paper) 0%, var(--card-paper-edge) 100%);
    overflow: hidden;
  }

  .edge-rule {
    position: absolute; top: 0; bottom: 0; width: 6px;
    background: var(--rule-white);
  }
  .edge-rule--left { left: 28px; }
  .edge-rule--right { right: 28px; }

  .brand { position: absolute; left: 60px; top: 62px; }
  .brand-square {
    width: 66px; height: 66px;
    background: var(--brand-red);
  }
  .brand-name {
    margin-top: 10px;
    color: var(--brand-red);
    font-weight: 700;
    font-size: 15px;
    letter-spacing: 0.5px;
  }

  .tagline {
    position: absolute; left: 180px; top: 70px;
    color: var(--brand-red);
    font-size: 30px;
    letter-spacing: 0.3px;
    white-space: nowrap;
  }

  .person { position: absolute; left: 60px; top: 248px; }
  .person-name {
    color: var(--brand-red);
    font-weight: 700;
    font-size: 25px;
  }
  .person-role {
    margin-top: 6px;
    color: var(--ink);
    font-size: 12.5px;
  }

  .address {
    position: absolute; left: 60px; top: 325px;
    display: flex; gap: 8px;
    color: var(--ink);
    font-size: 17px; line-height: 1.3;
  }
  .address svg { flex: none; margin-top: 3px; }

  .contact-list {
    position: absolute; left: 385px; top: 168px;
    list-style: none;
    color: var(--ink);
    font-size: 14.5px;
    white-space: nowrap;
  }
  .contact-list li {
    display: flex; align-items: center; gap: 10px;
    height: 22px;
  }
  .contact-list svg { flex: none; }
</style>
</head>
<body>

  <div class="card card-back" aria-label="Card back, solid brand red"></div>

  <article class="card card-front">
    <span class="edge-rule edge-rule--left"></span>
    <span class="edge-rule edge-rule--right"></span>

    <div class="brand">
      <div class="brand-square"></div>
      <div class="brand-name">Kelmorvo Group</div>
    </div>

    <p class="tagline">Listen - Shape - Deliver</p>

    <div class="person">
      <h1 class="person-name">Tom Harwick</h1>
      <p class="person-role">Partner - Head of Commercial Advisory</p>
    </div>

    <p class="address">
      <svg width="12" height="16" viewBox="0 0 12 16" aria-hidden="true">
        <path d="M6 0C2.7 0 0 2.6 0 5.8 0 10 6 16 6 16s6-6 6-10.2C12 2.6 9.3 0 6 0z" fill="var(--brand-red)"/>
        <circle cx="6" cy="5.8" r="2.2" fill="#fff"/>
      </svg>
      <span>Level 8, 214 Marlow St,<br>Fenwick, Vic 3999 Australia</span>
    </p>

    <ul class="contact-list">
      <li>
        <svg width="12" height="14" viewBox="0 0 12 14" aria-hidden="true"><rect x="3" y="0" width="6" height="14" rx="1" fill="var(--brand-red)"/><rect x="4" y="2" width="4" height="6" fill="#fff"/></svg>
        +61 400 555 017
      </li>
      <li>
        <svg width="12" height="14" viewBox="0 0 12 14" aria-hidden="true"><rect x="0" y="3" width="12" height="10" rx="1" fill="var(--brand-red)"/><rect x="2" y="1" width="3" height="4" fill="var(--brand-red)"/><rect x="6" y="5" width="4" height="2" fill="#fff"/></svg>
        +61 3 5550 1184
      </li>
      <li>
        <svg width="12" height="14" viewBox="0 0 12 14" aria-hidden="true"><rect x="3" y="1" width="6" height="4" fill="var(--brand-red)"/><rect x="0" y="5" width="12" height="6" rx="1" fill="var(--brand-red)"/><rect x="3" y="9" width="6" height="4" fill="var(--brand-red)" stroke="#fff" stroke-width="1"/></svg>
        +61 3 5550 1180
      </li>
      <li>
        <svg width="12" height="14" viewBox="0 0 12 14" aria-hidden="true"><rect x="0" y="3" width="12" height="8" fill="var(--brand-red)"/><path d="M0 3l6 5 6-5" fill="none" stroke="#fff" stroke-width="1"/></svg>
        tom.harwick@kelmorvo-grp.example
      </li>
      <li>
        <svg width="12" height="14" viewBox="0 0 12 14" aria-hidden="true"><circle cx="6" cy="7" r="6" fill="var(--brand-red)"/><path d="M0 7h12M6 1c-3 3-3 9 0 12M6 1c3 3 3 9 0 12" fill="none" stroke="#fff" stroke-width="0.8"/></svg>
        www.kelmorvo-grp.example
      </li>
    </ul>
  </article>

</body>
</html>
```